JT Holly Cleaning Business Card

We need a business card for our new business, a cleaning company using steam. We already have a logo, and would like a modern-looking card using colors that go well with those in our logo.

```html
<!DOCTYPE html>
<html lang="en">
<head>
<meta charset="utf-8">
<title>JT Holly Cleaning – Business Card</title>
<link href="https://fonts.googleapis.com/css2?family=Lato:wght@300;400;700;900&display=swap" rel="stylesheet">
<style>
  :root {
    --backdrop: #d9d9d9;
    --card-white: #ffffff;
    --green-light: #b9d630;
    --green-mid: #3f9a2c;
    --green-deep: #1f6a1f;
    --green-shadow: #0f4312;
    --brand-blue: #2f6fc4;
    --mark-green: #4ea52f;
    --text-light: #ffffff;
  }
  * { margin: 0; padding: 0; box-sizing: border-box; }
  html, body {
    width: 1200px;
    height: 926px;
    overflow: hidden;
    background: var(--backdrop);
    font-family: "Lato", Arial, sans-serif;
  }
  .canvas {
    position: relative;
    width: 1200px;
    height: 926px;
    display: flex;
    align-items: center;
    justify-content: center;
  }
  .business-card {
    position: relative;
    width: 1000px;
    height: 571px;
    background: var(--card-white);
    box-shadow: 0 18px 40px rgba(0,0,0,0.25);
    overflow: hidden;
  }
  .brand-band {
    position: absolute;
    top: 0; left: 0; right: 0;
    height: 208px;
    background: var(--card-white);
    display: flex;
    align-items: center;
    justify-content: center;
    gap: 22px;
  }
  .brand-mark {
    width: 84px;
    height: 84px;
    border-radius: 50%;
    background: var(--mark-green);
    flex: none;
  }
  .brand-name {
    font-weight: 900;
    font-size: 52px;
    color: var(--brand-blue);
    letter-spacing: 0.5px;
    line-height: 1;
    white-space: nowrap;
  }
  .contact-panel {
    position: absolute;
    top: 208px; left: 0; right: 0; bottom: 0;
    background:
      radial-gradient(ellipse 55% 70% at 38% 8%, var(--green-light) 0%, rgba(120,190,40,0.6) 35%, rgba(63,154,44,0) 75%),
      radial-gradient(ellipse 120% 130% at 45% 30%, var(--green-mid) 0%, var(--green-deep) 65%, var(--green-shadow) 100%);
    border-top: 6px solid var(--green-shadow);
    box-shadow: inset 0 10px 14px -8px rgba(0,0,0,0.45);
    color: var(--text-light);
    text-align: center;
    padding-top: 58px;
  }
  .person-name {
    font-size: 50px;
    font-weight: 300;
    line-height: 1;
    margin-bottom: 30px;
  }
  .person-name strong { font-weight: 700; }
  .contact-list {
    list-style: none;
    font-size: 25px;
    font-weight: 400;
    line-height: 1.5;
    white-space: nowrap;
  }
</style>
</head>
<body>
  <main class="canvas">
    <article class="business-card">
      <header class="brand-band">
        <span class="brand-mark" aria-hidden="true"></span>
        <span class="brand-name">JT Holly Cleaning</span>
      </header>
      <section class="contact-panel">
        <h1 class="person-name">Maria <strong>Lopez</strong></h1>
        <ul class="contact-list">
          <li>555-218-4370</li>
          <li>jthollyclean.com</li>
          <li>maria@jthollyclean.com</li>
          <li>48 Birch Lane Road, Suite #210, Elm Park, NY 10573</li>
        </ul>
      </section>
    </article>
  </main>
</body>
</html>
```